Business Card Design Project

We need a Business Card for an Mechanical Engineering firm in Singapore. The design should be Modern & Technical looking, yet eye catching.

Our company deals in Cutting Tools & Machine Accessories for the Manufacturing Industries such as Oil & Gas, Aero Space, etc... For more information on our Company, you can either email me or view our website www.valtrion.com.sg.

We are trying to revamp our image to give our consumers a fresh new perspective to our company, so we welcome all ideas.

Industry/Entity Type

Business

Requirements
Must have
• Must incorporate New Company Logo into the card as shown in Uploaded file.

```html
<!DOCTYPE html>
<html lang="en">
<head>
<meta charset="utf-8">
<title>Valtrion Tools – Business Card</title>
<link rel="stylesheet" href="https://fonts.googleapis.com/css2?family=Open+Sans:wght@400;600&display=swap">
<style>
  :root {
    --maroon: #8b1c24;
    --ink: #2f2f2f;
    --ink-soft: #4a4a4a;
    --charcoal: #2b2424;
    --card: #ffffff;
    --stage: #e7e7e7;
  }
  * { box-sizing: border-box; margin: 0; padding: 0; }
  html, body { width: 1200px; height: 944px; overflow: hidden; }
  body {
    background: var(--stage);
    font-family: "Open Sans", Arial, sans-serif;
    color: var(--ink);
    position: relative;
  }
  .card {
    position: absolute;
    width: 560px;
    height: 320px;
    background: var(--card);
    border-radius: 22px;
    overflow: hidden;
    box-shadow: 0 6px 18px rgba(0,0,0,0.18);
  }
  .card--front { left: 70px; top: 70px; }
  .card--back  { left: 570px; top: 550px; }

  .wordmark {
    position: absolute;
    display: flex;
    align-items: center;
    gap: 12px;
    color: var(--maroon);
    font-weight: 600;
    letter-spacing: 0.5px;
    white-space: nowrap;
  }
  .wordmark__dot {
    border-radius: 50%;
    background: var(--maroon);
    flex: none;
  }
  .card--front .wordmark { left: 52px; top: 176px; font-size: 36px; }
  .card--front .wordmark__dot { width: 26px; height: 26px; }
  .front-web {
    position: absolute;
    left: 330px; top: 248px;
    font-size: 17px;
    letter-spacing: 0.6px;
    color: var(--ink);
  }

  .card--back .wordmark { left: 46px; top: 48px; font-size: 24px; }
  .card--back .wordmark__dot { width: 18px; height: 18px; }
  .holder { position: absolute; left: 330px; top: 58px; }
  .holder__name { font-size: 19px; color: var(--ink); }
  .holder__role { font-size: 14px; font-style: italic; color: var(--maroon); }

  .address {
    position: absolute; left: 40px; top: 176px;
    font-size: 15px; line-height: 1.35; color: var(--ink-soft);
    display: flex; gap: 8px;
  }
  .contacts {
    position: absolute; left: 330px; top: 176px;
    list-style: none; font-size: 15px; line-height: 1.38; color: var(--ink-soft);
  }
  .contacts li { display: flex; align-items: center; gap: 8px; }
  .icon { width: 13px; height: 13px; flex: none; fill: var(--maroon); }
  .contacts .web { color: var(--ink); }
  .contacts .web span { color: var(--maroon); }
  .stripe { position: absolute; left: 0; bottom: 0; width: 560px; height: 34px; }
</style>
</head>
<body>

<section class="card card--front" aria-label="Business card front">
  <div class="wordmark"><span class="wordmark__dot"></span>VALTRION TOOLS</div>
  <p class="front-web">www.valtriontools.com</p>
</section>

<section class="card card--back" aria-label="Business card back">
  <div class="wordmark"><span class="wordmark__dot"></span>VALTRION TOOLS</div>
  <div class="holder">
    <p class="holder__name">Marcus Lenfield</p>
    <p class="holder__role">manager</p>
  </div>
  <div class="address">
    <svg class="icon" viewBox="0 0 14 14" aria-hidden="true"><path d="M7 1 L13 7 H11 V13 H8.5 V9 H5.5 V13 H3 V7 H1 Z"/></svg>
    <p>1480 Orchard Vale Rd.<br>Harlow, TX 78114</p>
  </div>
  <ul class="contacts">
    <li><svg class="icon" viewBox="0 0 14 14" aria-hidden="true"><path d="M3 1 L5.5 1 L6.5 4 L5 5.2 C5.8 7 7 8.2 8.8 9 L10 7.5 L13 8.5 V11 C13 12 12 13 11 13 C6 13 1 8 1 3 C1 2 2 1 3 1 Z"/></svg>512-004-2290</li>
    <li><svg class="icon" viewBox="0 0 14 14" aria-hidden="true"><rect x="3" y="1" width="8" height="12" rx="1.5"/><rect x="4.5" y="3" width="5" height="4" fill="#fff"/></svg>512-004-2291</li>
    <li><svg class="icon" viewBox="0 0 14 14" aria-hidden="true"><rect x="1" y="3" width="12" height="8" rx="1"/><path d="M1.5 3.5 L7 8 L12.5 3.5" stroke="#fff" stroke-width="1.2" fill="none"/></svg>info@valtriontools.com</li>
    <li class="web"><svg class="icon" viewBox="0 0 14 14" aria-hidden="true"><circle cx="7" cy="7" r="6"/></svg>www.<span>valtriontools</span>.com</li>
  </ul>
  <svg class="stripe" viewBox="0 0 560 34" preserveAspectRatio="none" aria-hidden="true">
    <polygon points="0,10 560,20 560,34 0,34" fill="var(--maroon)"/>
    <polygon points="430,20 560,20 560,34 400,34" fill="var(--charcoal)"/>
  </svg>
</section>

</body>
</html>
```